Web Design Project: Facility Management company

Hi! We need a new website.

Our current website: http://www.vireo-trade.ru/ and we don-t like it. =)
The structure of our company has changed and now we don't need "cleaning" and "engeneering" on this site.

We are facility management company in Russia. So we provide integrated service solutions specific to industrial services: maintenance, repair, etc. of engineering systems.
More services:
Energy planning
Automation
Audit
Statements with regulators
Video surveillance
Central heating
Security systems
Welding
Management of subcontractors
Electrical installation and service needs
Reception
Catering

Visitors:
* Managers in the field of commercial real estate
* Chief engineers
* TOP managers of large companies, malls, factories...
+ their subordinates
* Small% of applicants.

Here you can see some websites/patterns we liked:
http://www.kobalmire.ru/ (This is our competitor’s site, so our site shouldn’t be an exact copy))))
http://www.dwatqo.ru/
http://www.layoutfarrow.com/demo/24296.html
http://www.layoutfarrow.com/website-templates/10145.html

Style:
Light, hi-tech/minimalizm, the color palette should be based on the original site colors (Green + black + white). http://www.vireo-trade.ru/

Estimated sitemap:
1. Home
2. About Us
3. Company's policy
4. History + Achievements.
5. Certificates
6. Map of presence (Here you can use sample map in file "our projects")
7. Services
8. Portfolio
9. News or blog
10. Jobs
11. Contacts - with the feedback form (or the function "call to order")
12. English

Need a design pages: main page, page 404. The rest of the page could be created by general pattern.

Logo, navigation bar and contacts should be visible on all pages of a site.
Flash animation elements and buttons, etc. - not needed.

* We need to develop 3 websites, so we are looking for a long term cooperation.
Looking forward to your creativity =)

Must Have:
Clear, intuitive structure of web pages.
In the center - of pictures reflecting our main services (industrial theme). May be in rotation.
BUT! This banner (central picture) should not be a huge one =)
All relevant information should be visible at once without scrolling.

A possibility to place media files (presentations, video ...) and 2 banner links on the main page.

Font should be available in Cyrillic.
Updates

IMPORTANT!

Please notice that in thisdesign we don't need "cleaning" and "engeneering" on this site.

So don't use old block of 4pictures from our current website. We don't need it anymore. 

Thestructure of our company has changed and now we need some links (may be banners,may be something else) to our future cleaning website as well as engeneeringwebsite.
It should look like seperate (partner) companies, not like our sevices.

Regards, Vera.

Please don't forget that we need bilingual site.

So define language changing tool in your designs.

Industry/Entity Type

Industrial

```html
<!DOCTYPE html>
<html lang="en">
<head>
<meta charset="utf-8">
<title>Vireo Service — Integrated Facility Management</title>
<link href="https://fonts.googleapis.com/css2?family=Roboto+Condensed:wght@400;700&family=Arimo:wght@400&display=swap" rel="stylesheet">
<style>
:root{
  --green:#8fa62a;
  --green-light:#a9bd3e;
  --green-pale:#dbe89a;
  --ink:#222;
  --text:#555;
  --muted:#777;
  --line:#d8d8d8;
  --bar-top:#4a4b4d;
  --bar-bottom:#1c1d1f;
  --page:#f8f8f8;
  --white:#fff;
}
*{box-sizing:border-box;margin:0;padding:0}
html,body{width:1200px;height:819px;overflow:hidden}
body{background:var(--page);font-family:"Arimo",Arial,sans-serif;color:var(--text);position:relative}
a{color:inherit;text-decoration:none}
.cond{font-family:"Roboto Condensed","Arial Narrow",sans-serif}

/* header */
.header{position:absolute;left:0;top:0;width:1200px;height:111px;background:var(--white);border-bottom:1px solid var(--line)}
.brand{position:absolute;left:61px;top:30px;display:flex;align-items:center;gap:14px}
.brand-mark{width:26px;height:26px;background:var(--green-light)}
.brand-name{font-family:"Roboto Condensed",sans-serif;font-weight:400;font-size:40px;letter-spacing:6px;color:var(--ink)}
.lang{position:absolute;left:1005px;top:0;width:139px;height:29px;background:linear-gradient(var(--bar-top),var(--bar-bottom));border-radius:0 0 8px 8px;display:flex;font-family:"Roboto Condensed",sans-serif;font-size:16px;color:#eee;box-shadow:0 2px 3px rgba(0,0,0,.3)}
.lang span{flex:1;text-align:center;line-height:28px}
.lang .active{background:#555}
.phone{position:absolute;left:890px;top:52px;display:flex;align-items:center;gap:16px;font-family:"Roboto Condensed",sans-serif;font-size:29px;color:var(--green-light);letter-spacing:1px}

/* nav */
.nav{position:absolute;left:0;top:120px;width:1200px;height:42px;background:linear-gradient(var(--bar-top),var(--bar-bottom))}
.nav ul{list-style:none;position:absolute;left:58px;top:0;display:flex;height:42px;align-items:center}
.nav li{font-family:"Roboto Condensed",sans-serif;font-size:17px;color:#fff;text-transform:uppercase;padding-right:22px;margin-right:22px;border-right:1px solid #444;line-height:18px}
.nav li:last-child{border:0}
.search{position:absolute;left:913px;top:6px;width:204px;height:30px;background:#c9c9c9;border:1px solid #999;font-family:"Roboto Condensed",sans-serif;font-size:13px;font-weight:700;color:#555;padding:8px 13px;letter-spacing:.5px}
.search-icon{position:absolute;left:1113px;top:3px}

/* banner */
.banner{position:absolute;left:59px;top:174px;width:1086px;height:271px;background:var(--white);border:3px solid #e2e2e2}
.banner-photo{position:absolute;left:0;top:0;width:600px;height:265px;background:linear-gradient(90deg,#8e979c 0%,#b7c0c6 55%,#dfe3e6 85%,#fff 100%)}
.banner-title{position:absolute;right:52px;top:20px;text-align:right;font-family:"Roboto Condensed",sans-serif;font-size:37px;line-height:41px;color:var(--green);letter-spacing:1.5px}
.banner-text{position:absolute;right:52px;top:126px;width:410px;text-align:justify;font-family:"Roboto Condensed",sans-serif;font-size:14.5px;line-height:27px;color:var(--muted);text-transform:uppercase;letter-spacing:.6px}

/* news */
.news-tab{position:absolute;left:74px;top:464px;width:89px;height:33px;background:var(--green-pale);border:3px solid var(--green-light);font-size:16px;color:#111;text-align:center;line-height:28px}
.news{position:absolute;left:63px;top:502px;width:301px;height:213px;background:var(--white);border:1px solid #ddd;padding:6px 8px 0 10px}
.news-item{position:relative;padding:6px 0 8px 21px;font-size:13.5px;line-height:20px;color:#666;text-align:justify;border-bottom:1px solid #bbb;height:75px;overflow:hidden}
.news-item:last-child{border:0;height:54px}
.news-item::before{content:"";position:absolute;left:2px;top:12px;border:5px solid transparent;border-left:6px solid #777;border-right:0}

/* welcome */
.welcome{position:absolute;left:394px;top:462px;width:467px}
.welcome h1{font-family:"Roboto Condensed",sans-serif;font-weight:400;font-size:22px;line-height:27px;color:var(--green);text-transform:uppercase;letter-spacing:.5px;margin-left:2px}
.welcome ul{list-style:none;margin-top:14px;margin-left:2px}
.welcome li{position:relative;padding-left:14px;font-size:13.5px;line-height:20px;color:#666}
.welcome li::before{content:"";position:absolute;left:0;top:6px;border:4px solid transparent;border-left:5px solid #888;border-right:0}
.welcome p{margin-top:20px;font-size:13.5px;line-height:20px;color:#666;text-align:justify}
.welcome p a{color:#000;text-decoration:underline}

/* video */
.video-head{position:absolute;left:887px;top:462px;width:260px;display:flex;align-items:center;gap:6px;font-size:18px;color:#555}
.video-head::before,.video-head::after{content:"";flex:1;height:3px;background:#333}
.video{position:absolute;left:885px;top:493px;width:263px;height:230px;border:1px solid var(--green-light);padding:2px;background:var(--white)}
.video-frame{width:100%;height:100%;background:linear-gradient(135deg,#d6df8a,#c9d474 60%,#b7c163);position:relative}
.video-play{position:absolute;left:50%;top:50%;transform:translate(-50%,-50%)}

/* footer */
.footer{position:absolute;left:0;top:736px;width:1200px;height:72px;background:linear-gradient(#1c1d1f,#444548);text-align:center;color:#fff}
.footer-links{margin-top:16px;font-size:13.5px}
.footer-links span{margin:0 9px}
.footer-copy{margin-top:8px;font-size:11.5px}
</style>
</head>
<body>

<header class="header">
  <div class="brand"><span class="brand-mark"></span><span class="brand-name">VIREO SERVICE</span></div>
  <div class="lang"><span>RUS</span><span class="active">ENG</span></div>
  <div class="phone">
    <svg width="26" height="30" viewBox="0 0 26 30" aria-hidden="true"><path d="M6 2 L11 3 L12 9 L9 11 Q11 18 16 22 L19 19 L24 22 L23 27 Q18 30 12 24 Q3 15 4 6 Z" fill="none" stroke="#7a8a22" stroke-width="2"/><path d="M2 28 H24" stroke="#7a8a22" stroke-width="2"/></svg>
    <span>+7 812 555 0148</span>
  </div>
</header>

<nav class="nav">
  <ul>
    <li>Home</li><li>About us</li><li>History</li><li>Services</li><li>Portfolio</li><li>Jobs</li><li>Contact us</li>
  </ul>
  <div class="search">SEARCH...</div>
  <svg class="search-icon" width="34" height="34" viewBox="0 0 34 34" aria-hidden="true"><circle cx="20" cy="13" r="9" fill="none" stroke="#fff" stroke-width="3"/><path d="M13 20 L4 29" stroke="#fff" stroke-width="5" stroke-linecap="round"/></svg>
</nav>

<section class="banner">
  <div class="banner-photo" role="img" aria-label="Photo of an industrial pump room with stainless steel tanks and a blue pump"></div>
  <h2 class="banner-title">INTEGRATED FACILITY<br>MANAGEMENT</h2>
  <p class="banner-text">Lorem ipsum dolor sit amet, consectetur adipiscing elit. Donec adipiscing dolor a magna consequat dapibus. Praesent non ante id nisi aliquam placerat. Phasellus porta vulputate bibendum.</p>
</section>

<div class="news-tab">NEWS</div>
<section class="news">
  <div class="news-item">Lorem ipsum dolor sit amet, consectetur adipiscing elit. Donec adipiscing dolor a magna consequat dapibus. Praesent non</div>
  <div class="news-item">Lorem ipsum dolor sit amet, consectetur adipiscing elit. Donec adipiscing dolor a magna consequat dapibus. Praesent non</div>
  <div class="news-item">Lorem ipsum dolor sit amet, consectetur adipiscing elit. Donec adipiscing dolor a</div>
</section>

<section class="welcome">
  <h1>Welcome to Vireo Services<br>Engineering Systems</h1>
  <ul>
    <li>Commercial property management</li>
    <li>Complex maintenance of immovable property</li>
    <li>Commercial property maintenance service</li>
  </ul>
  <p>These are the most important aspects of acquisition of the highest possible incomes from the commercial property object`s operation regardless of their purpose: it can be production, business center, a building of a shop, bank, restaurant, warehousing logistic complex, hotel or the biggest shopping and recreation center. <a href="#">More...</a></p>
</section>

<div class="video-head">VIDEO</div>
<section class="video">
  <div class="video-frame" role="img" aria-label="Video preview of engineering drawings with drafting tools, tinted green">
    <svg class="video-play" width="64" height="64" viewBox="0 0 64 64" aria-hidden="true"><circle cx="32" cy="32" r="29" fill="#222" stroke="#999" stroke-width="3"/><path d="M26 20 L42 32 L26 44 Z" fill="#fff"/></svg>
  </div>
</section>

<footer class="footer">
  <div class="footer-links">Company<span>|</span>Chosen by<span>|</span>Contact us<span>|</span>Integrated facility management<span>|</span>Technical maintenance of engineering systems<span>|</span>Company policy</div>
  <div class="footer-copy">All rights reserved @ vireo-trade.ru</div>
</footer>

</body>
</html>
```